Wordpress template for a mens-choire webpage

Task is to design a Wordpress template for an 98 years old estonian mens choire webpage.
Design should involve details from the attached files, choire logo and the colors of the choire flag: in horizontal orientation bright sky-blue, white, bright grass-green.
Designer signature is allowed to be added to the template, with country of origin.

Reason: Deadline extended 2 days (until 2. March 2014) to accommodate designers creativity.

Thank you everyone for your great designs!
Our project has now entered into a voting and decision phase until 14th of March 2014 (included).

```html
<!DOCTYPE html>
<html lang="en">
<head>
<meta charset="utf-8">
<title>Kalda Meeskoor</title>
<link rel="stylesheet" href="https://fonts.googleapis.com/css2?family=Source+Sans+3:wght@400;600&display=swap">
<style>
:root{
  --teal:#3fb3ad;
  --teal-dark:#3a8f8b;
  --ink:#333333;
  --muted:#9aa089;
  --olive:#56603f;
  --cream:#f6ecd8;
  --gold:#c8952f;
  --footer:#232323;
  --footer-base:#0f0f0f;
  --white:#ffffff;
  --line:#e6e6e6;
}
*{box-sizing:border-box;margin:0;padding:0}
html,body{width:800px;height:1200px;overflow:hidden}
body{position:relative;background:var(--white);font-family:"Source Sans 3",sans-serif;color:var(--ink);font-size:9px;line-height:1.35}
.abs{position:absolute}
a{color:inherit;text-decoration:none}

.hero{left:0;top:0;width:800px;height:447px;background:linear-gradient(180deg,#7fb0a6 0%,#9cb39a 28%,#c9a57e 55%,#c0675a 82%,#b2433f 100%)}
.topbar{left:0;top:0;width:800px;height:30px;background:rgba(40,80,80,.55);border-bottom:1px solid rgba(255,255,255,.25)}
.topbar .contacts{right:79px;top:9px;display:flex;gap:20px;white-space:nowrap}
.topbar .contact{font-size:10px;color:#cfe0dc;display:flex;align-items:center;gap:6px}
.brand{left:82px;top:88px;display:flex;align-items:center;gap:8px;color:var(--white);font-size:16px;font-weight:600}
.brand .dot{width:22px;height:22px;border-radius:50%;background:var(--white)}
.search{left:583px;top:65px;width:137px;height:18px;background:var(--white)}
.nav{left:407px;top:102px;display:flex;gap:21px;font-size:14px;font-weight:600;color:var(--white)}
.slide{left:115px;top:183px;width:572px;height:208px;background:radial-gradient(ellipse at 35% 40%,#fffaf0,var(--cream));border-radius:6px}
.slide h1{left:26px;top:22px;width:230px;font-size:18px;line-height:24px;font-weight:600;color:var(--olive)}
.slide p{left:26px;top:106px;width:240px;font-size:11px;line-height:13.5px;color:var(--muted)}
.dots{left:26px;top:157px;display:flex;gap:5px}
.dots span{width:9px;height:9px;border-radius:50%;background:var(--gold)}
.frame{left:394px;top:145px;width:268px;height:225px;background:#e4e4e4;border-radius:8px;box-shadow:0 2px 6px rgba(0,0,0,.35)}
.frame .photo{left:9px;top:8px;width:250px;height:207px;border-radius:4px;background:linear-gradient(160deg,#5e3a22,#8a5a34 45%,#2c2a4a 80%)}
.arrow{top:257px;width:60px;height:60px;border-radius:50%;background:rgba(110,80,55,.55)}

.welcome h2{left:81px;top:472px;font-size:16px;font-weight:400;color:var(--teal)}
.welcome p{left:81px;width:360px;font-size:9px;line-height:11.3px}
.btn{background:linear-gradient(#6cbdbb,var(--teal-dark));color:var(--white);border-radius:3px;text-align:center}
.video{left:489px;top:473px;width:232px;height:119px;border-radius:6px;background:linear-gradient(180deg,#1c1c1c,#3b3328 60%,#0c0c0c)}
.divider{left:130px;width:540px;height:1px;background:linear-gradient(90deg,transparent,var(--line),transparent)}

.card{top:673px;width:146px}
.card .img{width:146px;height:110px;position:relative}
.card .label{position:absolute;left:0;top:0;width:100%;height:32px;background:rgba(20,20,20,.7);color:var(--white);font-size:11px;padding:10px 0 0 14px}
.card p{margin-top:13px;font-size:9px;line-height:10.5px}
.card .more{display:block;margin-top:14px;color:var(--teal-dark);font-weight:600;font-size:9px}

.section-title{font-size:11px;color:var(--teal)}
.blog-img{left:81px;top:949px;width:146px;height:81px;border-radius:4px;background:linear-gradient(135deg,#7a4a26,#d8b27a 50%,#5a3a22)}
.field{left:575px;width:146px;height:21px;border:1px solid #ddd;border-radius:3px;color:#aaa;font-size:8px;padding:5px 8px}

.footer{left:0;top:1075px;width:800px;height:111px;background:var(--footer);color:var(--white)}
.footer h3{font-size:13px;font-weight:400;margin-bottom:3px}
.footer ul{list-style:none;font-size:9px;line-height:11.3px}
.footer .col{top:12px}
.footer .sep{top:28px;width:1px;height:72px;background:#3c3c3c}
.social{display:flex;gap:11px}
.social span{width:21px;height:21px;border-radius:2px}
.base{left:0;top:1186px;width:800px;height:14px;background:var(--footer-base);color:#ddd;font-size:7px;text-align:center;line-height:14px}
</style>
</head>
<body>

<header class="abs hero">
  <div class="abs topbar">
    <div class="abs contacts">
      <div class="contact">
        <svg width="12" height="9" viewBox="0 0 12 9"><rect x="0.5" y="0.5" width="11" height="8" fill="none" stroke="#cfe0dc"/><path d="M0.5 0.5 6 5 11.5 0.5" fill="none" stroke="#cfe0dc"/></svg>
        info@kaldachoir.example
      </div>
      <div class="contact">
        <svg width="8" height="12" viewBox="0 0 8 12"><rect x="0.5" y="0.5" width="7" height="11" rx="1.5" fill="none" stroke="#cfe0dc"/></svg>
        0800 4417 302
      </div>
    </div>
  </div>
  <div class="abs brand"><span class="dot"></span>Kalda Meeskoor</div>
  <div class="abs search">
    <svg class="abs" style="right:3px;top:2px" width="14" height="14" viewBox="0 0 14 14"><circle cx="6" cy="6" r="4.5" fill="none" stroke="#7a9a95" stroke-width="1.6"/><path d="M9.3 9.3 13 13" stroke="#7a9a95" stroke-width="1.8"/></svg>
  </div>
  <nav class="abs nav"><a>HOME</a><a>ABOUT</a><a>BLOG</a><a>GALLERY</a><a>CONTACT</a></nav>

  <div class="abs slide">
    <h1 class="abs">LOREM IPSUM DOLOR SIT AMET CONSECTETUER ADIPISCING ELIT</h1>
    <p class="abs">Sed diam nonummy nibh euismod tincidunt ut laoreet dolore magna aliquam erat volutpat. enim ad minim veniam, quis nostrud exerci tation.</p>
    <div class="abs dots"><span></span><span></span><span></span></div>
  </div>
  <div class="abs frame"><div class="abs photo" role="img" aria-label="Choir singing in a cathedral choir stall"></div></div>
  <div class="abs arrow" style="left:81px"><svg width="60" height="60" viewBox="0 0 60 60"><path d="M33 21 25 30 33 39" fill="none" stroke="#fff" stroke-width="3.5"/></svg></div>
  <div class="abs arrow" style="left:660px"><svg width="60" height="60" viewBox="0 0 60 60"><path d="M27 21 35 30 27 39" fill="none" stroke="#fff" stroke-width="3.5"/></svg></div>
</header>

<section class="welcome">
  <h2 class="abs">Welcome to our site</h2>
  <p class="abs" style="top:501px">Lorem ipsum dolor sit amet, consectetuer adipiscing elit, sed diam nonummy nibh euismod tincidunt ut laoreet dolore magna aliquam erat volutpat. Ut wisi enim ad minim veniam, uis nostrud exerci tation ullamcorper suscipit lobortis nisl ut aliquip ex ea commodo consequat. Duis autem vel eum iriure dolor in hendrerit in vulputate.</p>
  <p class="abs" style="top:554px">Lorem ipsum dolor sit amet, consectetuer adipiscing elit, sed diam nonummy nibh euismod tincidunt ut laoreet dolor.</p>
  <a class="abs btn" style="left:81px;top:589px;width:72px;height:24px;line-height:24px;font-size:8px">Read More</a>
  <div class="abs video" role="img" aria-label="Video of the choir performing on stage">
    <svg class="abs" style="left:96px;top:39px" width="42" height="42" viewBox="0 0 42 42"><circle cx="21" cy="21" r="19" fill="none" stroke="#fff" stroke-width="2.5"/><path d="M16 12 30 21 16 30Z" fill="#fff"/></svg>
  </div>
</section>

<div class="abs divider" style="top:633px"></div>

<section>
  <article class="abs card" style="left:81px"><div class="img" role="img" aria-label="Choir on a concert hall stage" style="background:linear-gradient(180deg,#3a2a1c,#8a5030 60%,#b0302a)"><span class="label">Join our chorus</span></div><p>Duis autem vel eum iriure dolor in hendrerit in vulputate velit esse molestie consequat, vel illum dolore eu feugiat nulla facilisis at vero eros.</p><a class="more">Read More</a></article>
  <article class="abs card" style="left:245px"><div class="img" role="img" aria-label="Choir rehearsing in a hall" style="background:linear-gradient(180deg,#4a3a2a,#a89070 55%,#6a5040)"><span class="label">Buy tickets</span></div><p>Duis autem vel eum iriure dolor in hendrerit in vulputate velit esse molestie consequat, vel illum dolore eu feugiat nulla facilisis at vero eros.</p><a class="more">Read More</a></article>
  <article class="abs card" style="left:409px"><div class="img" role="img" aria-label="Singers reading sheet music" style="background:linear-gradient(135deg,#2a2a2a,#c8b0a0 55%,#e8e0d8)"><span class="label">Learn with us</span></div><p>Duis autem vel eum iriure dolor in hendrerit in vulputate velit esse molestie consequat, vel illum dolore eu feugiat nulla facilisis at vero eros.</p><a class="more">Read More</a></article>
  <article class="abs card" style="left:574px"><div class="img" role="img" aria-label="Church interior with altar" style="background:linear-gradient(180deg,#3a3024,#b07838 55%,#6a4426)"><span class="label">Whats's new</span></div><p>Duis autem vel eum iriure dolor in hendrerit in vulputate velit esse molestie consequat, vel illum dolore eu feugiat nulla facilisis at vero eros.</p><a class="more">Read More</a></article>
</section>

<div class="abs divider" style="top:893px"></div>

<section>
  <h4 class="abs section-title" style="left:81px;top:922px;font-weight:400">Recent Blog Posts</h4>
  <div class="abs blog-img" role="img" aria-label="Group of choir members together"></div>
  <h5 class="abs" style="left:245px;top:955px;font-size:11px;font-weight:400;color:var(--teal)">Duis autem vel eum iriure dolor in hendrerit</h5>
  <div class="abs" style="left:245px;top:970px;font-size:8px">Feb 27, 2014</div>
  <p class="abs" style="left:245px;top:985px;width:302px;font-size:9px;line-height:10.6px">Vulputate velit esse molestie consequat, vel illum dolore eu feugiat nulla facilisis at vero eros et accumsan et iusto odio dignissim qui blandit Duis autem vel eum iriure dolor in hendrerit in vulputate velit esse molestie consequat, vel illum dolore eu feugiat nulla facilisis at vero eros et aan et iusto dignissim...<span style="color:var(--teal)">READ MORE</span></p>

  <h4 class="abs section-title" style="left:575px;top:922px;font-weight:400">Sign Up for Newsletters</h4>
  <div class="abs field" style="top:949px">Full Name</div>
  <div class="abs field" style="top:976px">Email Address</div>
  <a class="abs btn" style="left:575px;top:1010px;width:57px;height:18px;line-height:18px;font-size:8px">Submit</a>
</section>

<footer class="abs footer">
  <div class="abs col" style="left:81px"><h3>Quick links</h3><ul><li>Home</li><li>About</li><li>Blog</li><li>Gallery</li><li>Videos</li><li>Contact</li></ul></div>
  <div class="abs sep" style="left:170px"></div>
  <div class="abs col" style="left:215px"><h3>Support us</h3><ul><li>Home</li><li>About</li><li>Blog</li><li>Gallery</li><li>Videos</li><li>Contact</li></ul></div>
  <div class="abs sep" style="left:316px"></div>
  <div class="abs col" style="left:357px"><h3>Contact us</h3><ul><li>12 Lindenweg. Haus 8</li><li>10115 Berlin Germany</li><li>Phone: 0800 4417 356</li><li>Email: info@kaldachoir.example</li></ul></div>
  <div class="abs sep" style="left:537px"></div>
  <div class="abs col" style="left:575px"><h3>Connect with us</h3>
    <div class="social" style="margin-top:12px"><span style="background:#3b5998"></span><span style="background:#2a9ad8"></span><span style="background:#c9402f"></span><span style="background:#c4302b"></span></div>
  </div>
</footer>
<div class="abs base">Copyright © 2014 Kalda Meeskoor.</div>

</body>
</html>
```